Logo and website for K-12 Academy- Lumora Pathis Academy

Overview
Lumora Pathis Academy is a new online educational institution based in Ghana & Portugal, offering a K-12 curriculum designed to empower the next generation with academic excellence, leadership skills, and deep-rooted cultural values. The academy emphasizes knowledge, mentorship, leadership, and a strong connection to African heritage.

Objective
Create a meaningful, timeless, and visually compelling logo that:

Represents growth, wisdom, and resilience through the imagery of the Odum Tree.

Symbolizes knowledge and academic pursuit.

Reflects mentorship and leadership development.

Appeals to parents and students alike, exuding trust, strength, and inspiration.

Key Themes
Odum Tree: A powerful symbol in Ghana, representing strength, endurance, and wisdom.

Knowledge: Books, light, open pathways, or abstract symbols of learning.

Mentorship/Leadership: Hands guiding others, rising figures, light leading the way, or interconnected branches.

Ghanaian Heritage: Subtle inclusion of Ghanaian cultural elements (such as color palette or patterns) without overwhelming the global, professional appeal.

Target Audience
Parents and guardians seeking quality education steeped in both academic rigor and cultural values.
Students from kindergarten through high school (ages 4–18).
Stakeholders and partners supporting education initiatives in Africa.

Style & Tone
Professional and Inspirational: Serious but welcoming.
Modern with Cultural Depth: Clean lines, minimal clutter, but with depth and meaning.
Warm and Trustworthy: The logo should evoke feelings of safety, hope, growth, and pride.
Flexible: It should work well in both full-color and monochrome versions, and look good at both large and small scales. Except for color changes and cultural elements, main logo should be able to be adapted to both countries
Color Palette (Suggestions)
Earth tones: Browns, greens — representing the Odum tree and growth
Gold/Yellow: For wisdom, enlightenment, and a nod to Ghana’s national colors.
Deep Red or Burgundy: Representing strength and heritage.
Logo Elements
Tree: Odum tree as the main, central symbol. Book, Light, or Path: Sub-elements to subtly symbolize knowledge and learning.
Mentorship: Perhaps visualized through multiple branches, a larger tree protecting smaller saplings, or guiding light themes.

Deliverables
Primary logo (full-color)
Secondary logo (single-color or black/white version)
Icon or emblem version (simplified for small applications like favicons or social media)
Logo usage guidelines (optional but preferred)

Target Market(s)

K-12 parents

Industry/Entity Type

Education

Coding

Coded - Design and coding required

Number of Pages Required

1 page

Font styles to use
Sans Serif

Requirements
Nice to have
• Inspirations Cultural motifs reimagined in a sleek, contemporary style. Nature-inspired logos that convey growth and resilience.

```html
<!DOCTYPE html>
<html lang="en">
<head>
<meta charset="utf-8">
<title>Lumora Pathis Academy</title>
<link href="https://fonts.googleapis.com/css2?family=Lexend:wght@400;500&family=Poppins:wght@400;500;600&display=swap" rel="stylesheet">
<style>
:root{
  --orange:#f5a623;
  --orange-deep:#f47a20;
  --green:#377a36;
  --green-soft:#56b06a;
  --olive:#8c8a2e;
  --ink:#222;
  --text:#333;
  --muted:#777;
  --grey-bg:#f4f4f4;
  --white:#fff;
}
*{margin:0;padding:0;box-sizing:border-box}
html,body{width:1200px;height:3913px;overflow:hidden;background:var(--white)}
body{font-family:"Poppins",sans-serif;color:var(--text)}
.page{position:relative;width:1200px;height:3913px;overflow:hidden}
.abs{position:absolute}
.heading{font-family:"Lexend",sans-serif;font-weight:500;color:var(--ink);font-size:36px;line-height:40px}
.copy{font-size:12px;line-height:19.7px;color:var(--text)}
.btn{position:absolute;display:flex;align-items:center;justify-content:center;font-size:12px;font-weight:500;color:var(--white);background:var(--orange)}
.media{position:absolute}
.ornament{position:absolute;border-radius:14px;opacity:.85}
.ornament.orange{background:var(--orange)}
.ornament.green{background:var(--green)}
.ornament.green-soft{background:var(--green-soft)}

/* header + hero */
.hero{position:absolute;left:0;top:0;width:1200px;height:574px;background:linear-gradient(135deg,#8a8c83 0%,#6f6552 40%,#9a8a6a 70%,#6c6a5a 100%)}
.hero-shade{position:absolute;inset:0;background:rgba(0,0,0,.28)}
.brand{position:absolute;left:120px;top:14px;width:120px;text-align:center;color:var(--white)}
.brand-mark{width:34px;height:34px;border-radius:50%;background:var(--white);margin:0 auto 4px}
.brand-name{font-size:15px;line-height:17px;font-weight:400}
.nav{position:absolute;left:284px;top:22px;display:flex;gap:34px;align-items:center;font-size:12px;color:var(--white)}
.nav-cta{position:absolute;left:994px;top:9px;width:117px;height:44px}
.hero-title{position:absolute;left:0;width:1200px;top:220px;text-align:center;font-family:"Lexend",sans-serif;font-weight:500;font-size:70px;line-height:84px;color:var(--white)}
.hero-sub{position:absolute;left:0;width:1200px;top:300px;text-align:center;font-size:19px;color:var(--white)}

/* footer */
.foot-h{font-family:"Lexend",sans-serif;font-weight:400;font-size:16px;letter-spacing:.5px;color:var(--ink)}
.foot-link{position:absolute;font-size:11.5px;color:#555}
.foot-small{font-size:11px;line-height:16px;color:var(--muted)}
.social{position:absolute;top:3873px;width:27px;height:27px;background:var(--orange-deep)}
</style>
</head>
<body>
<div class="page">

  <!-- Hero -->
  <section class="hero" role="img" aria-label="Photo of children and a teacher exploring planet models at a classroom table">
    <div class="hero-shade"></div>
  </section>
  <div class="ornament orange" style="left:222px;top:135px;width:36px;height:36px" role="img" aria-label="Decorative orange leaf shape"></div>
  <div class="ornament orange" style="left:412px;top:150px;width:34px;height:40px" role="img" aria-label="Decorative orange leaf shape"></div>
  <div class="ornament green" style="left:230px;top:296px;width:32px;height:42px" role="img" aria-label="Decorative green leaf shape"></div>
  <div class="ornament green" style="left:806px;top:110px;width:64px;height:62px" role="img" aria-label="Decorative green speech bubble"></div>
  <div class="ornament green" style="left:920px;top:280px;width:60px;height:60px" role="img" aria-label="Decorative green speech bubble"></div>

  <div class="brand">
    <div class="brand-mark"></div>
    <div class="brand-name">Lumora Pathis<br><span style="font-size:11px">Academy</span></div>
  </div>
  <nav class="nav">
    <svg width="14" height="13" viewBox="0 0 14 13"><path d="M7 0 L14 6 H12 V13 H9 V9 H5 V13 H2 V6 H0z" fill="var(--orange)"/></svg>
    <span>About Us</span><span>Our Approach</span><span>Admissions</span><span>Academics</span><span>Community Life</span><span>News &amp; Blog</span>
  </nav>
  <a class="btn nav-cta">Contact Us</a>
  <h1 class="hero-title">Lumora Pathis</h1>
  <p class="hero-sub">Academy is a new online educational institution</p>
  <a class="btn" style="left:472px;top:351px;width:118px;height:43px">Apply Now</a>
  <a class="btn" style="left:600px;top:351px;width:117px;height:43px;background:var(--green)">Contact Us</a>

  <!-- Intro -->
  <div class="media" style="left:1033px;top:608px;width:167px;height:273px;background:linear-gradient(160deg,#5b9be0,#f0b73a);opacity:.8" role="img" aria-label="Illustration of a blue and yellow kite with a ribboned tail"></div>
  <h2 class="heading abs" style="left:204px;top:718px">Where Knowledge<br>Meets Life.</h2>
  <div class="media" style="left:87px;top:813px;width:121px;height:121px;border-radius:50%;background:radial-gradient(circle,#f7c63a 55%,#fbe7b3 100%)" role="img" aria-label="Illustration of a smiling cartoon sun"></div>
  <div class="media" style="left:243px;top:808px;width:281px;height:202px;background:linear-gradient(135deg,#fbe1cf,#cfe8f3);border-radius:12px" role="img" aria-label="Illustration of a cartoon boy with hand lettering reading Where Leaders Are Born"></div>
  <div class="copy abs" style="left:588px;top:696px;width:366px">
    <p>At Lumora Pathis Academy, we're reimagining education for the 21st century by returning to timeless wisdom: children learn best in mixed-age communities where knowledge is practical, leadership is developed through mentorship, and every student both teaches and learns.</p>
    <p style="margin-top:14px">At Lumora Pathis Academy, we're reimagining education for the 21st century by returning to timeless wisdom: children learn best in mixed-age communities where knowledge is practical, leadership</p>
  </div>
  <a class="btn" style="left:586px;top:920px;width:119px;height:43px">Read More</a>
  <div class="ornament green-soft" style="left:712px;top:876px;width:70px;height:64px" role="img" aria-label="Decorative green speech bubble"></div>

  <!-- Approach band -->
  <section class="abs" style="left:0;top:1077px;width:1200px;height:1440px;background:var(--grey-bg)"></section>

  <svg class="abs" style="left:0;top:0" width="1200" height="2600" aria-hidden="true">
    <path d="M197 1244 A185 185 0 0 0 325 1519" fill="none" stroke="var(--green)" stroke-width="10" stroke-linecap="round"/>
    <path d="M341 1153 A185 185 0 0 1 531 1400" fill="none" stroke="var(--green)" stroke-width="7" stroke-linecap="round"/>
    <path d="M812 1852 A185 185 0 0 1 676 1562" fill="none" stroke="var(--orange)" stroke-width="10" stroke-linecap="round"/>
    <path d="M765 1494 A185 185 0 0 1 1001 1606" fill="none" stroke="var(--orange)" stroke-width="7" stroke-linecap="round"/>
    <path d="M195 2041 A185 185 0 0 0 353 2288" fill="none" stroke="var(--green)" stroke-width="10" stroke-linecap="round"/>
    <path d="M339 1932 A185 185 0 0 1 531 2011" fill="none" stroke="var(--green)" stroke-width="7" stroke-linecap="round"/>
  </svg>
  <div class="ornament green" style="left:158px;top:1145px;width:64px;height:66px" role="img" aria-label="Decorative green leaf shape"></div>
  <div class="ornament green" style="left:1004px;top:1440px;width:80px;height:60px" role="img" aria-label="Decorative green speech bubble"></div>
  <div class="ornament orange" style="left:500px;top:1823px;width:74px;height:74px" role="img" aria-label="Decorative orange blob"></div>

  <div class="media" style="left:182px;top:1162px;width:350px;height:350px;border-radius:50%;background:linear-gradient(135deg,#8b5a3c,#d9a25c 60%,#e05a3a)" role="img" aria-label="Photo of two young boys building with colourful blocks"></div>
  <h2 class="heading abs" style="left:630px;top:1209px">Our Unique Approach</h2>
  <p class="copy abs" style="left:633px;top:1262px;width:390px">Our innovative "Family Units" bring together students from kindergarten through grade 10 in small, supportive learning communities. Unlike traditional classrooms where children are segregated by age, our approach mirrors real life, where collaboration across generations creates powerful learning opportunities.</p>
  <a class="btn" style="left:633px;top:1404px;width:118px;height:44px">Read More</a>

  <h2 class="heading abs" style="left:182px;top:1595px">Practical Knowledge,<br>Real-World Skills</h2>
  <p class="copy abs" style="left:185px;top:1677px;width:430px">At LPA, education extends beyond textbooks. Our students don't just study engineering—they build solutions to community challenges. They don't just learn business concepts—they create and operate their own enterprises. From our state-of-the-art maker spaces to our environmental stewardship programs, learning is hands-on, meaningful, and connected to real needs.</p>
  <a class="btn" style="left:185px;top:1820px;width:117px;height:44px">Read More</a>
  <div class="media" style="left:656px;top:1496px;width:344px;height:344px;border-radius:50%;background:linear-gradient(135deg,#e8c8b8,#2f5fa8 55%,#f2f2f2)" role="img" aria-label="Photo of a boy in a striped shirt drawing at a desk"></div>

  <div class="media" style="left:194px;top:1929px;width:350px;height:350px;border-radius:50%;background:linear-gradient(135deg,#5a3a2a,#efe8a0 55%,#d8454a)" role="img" aria-label="Photo of a girl with braided hair writing in class"></div>
  <h2 class="heading abs" style="left:632px;top:1936px">A Curriculum for Future<br>Innovators</h2>
  <p class="copy abs" style="left:634px;top:2018px;width:440px">Our academic framework balances core skills with creative expression, technological literacy, and cultural understanding. Students progress through three developmental phases:</p>
  <div class="abs copy" style="left:634px;top:2089px;width:440px">
    <p style="font-weight:600;color:var(--ink)"><span style="display:inline-block;width:9px;height:9px;border-radius:50%;background:var(--orange);margin-right:10px"></span>Foundation Phase</p>
    <p style="padding-left:19px">(K-Grade 3): Building core skills while discovering the joy of learning</p>
    <p style="font-weight:600;color:var(--ink);margin-top:10px"><span style="display:inline-block;width:9px;height:9px;border-radius:50%;background:var(--orange);margin-right:10px"></span>Development Phase</p>
    <p style="padding-left:19px">(Grades 4-7): Deepening knowledge while beginning mentorship responsibilities</p>
    <p style="font-weight:600;color:var(--ink);margin-top:10px"><span style="display:inline-block;width:9px;height:9px;border-radius:50%;background:var(--orange);margin-right:10px"></span>Leadership Phase</p>
    <p style="padding-left:19px">(Grades 8-10): Mastering advanced concepts while leading projects and mentoring younger students</p>
  </div>

  <!-- Enquiry wave -->
  <svg class="abs" style="left:0;top:2300px" width="1200" height="640" aria-hidden="true">
    <path d="M0 92 C250 40 600 30 820 40 C1020 50 1130 160 1130 320 C1130 470 1090 560 1040 590 C900 560 700 520 450 560 C250 590 80 600 0 610 Z" fill="var(--green)"/>
  </svg>
  <div class="ornament orange" style="left:886px;top:2413px;width:90px;height:70px" role="img" aria-label="Decorative orange speech bubble"></div>
  <div class="media" style="left:61px;top:2460px;width:425px;height:426px;border-radius:50% 50% 0 0;background:linear-gradient(160deg,#4a2e22,#e1a27a 40%,#3aa7de 80%)" role="img" aria-label="Photo of a smiling girl in a blue shirt"></div>
  <h2 class="heading abs" style="left:530px;top:2459px;color:var(--white)">Nurture Your Child's<br>Potential.</h2>
  <p class="abs" style="left:533px;top:2545px;width:340px;font-size:12px;line-height:20px;color:var(--white)">Reach out today to learn if the Lumora Learning Hub is a fit for your family's needs</p>
  <div class="abs" style="left:532px;top:2599px;width:348px;height:27px;background:var(--olive);color:var(--white);font-size:10px;padding:8px 22px">Name</div>
  <div class="abs" style="left:532px;top:2636px;width:348px;height:27px;background:var(--olive);color:var(--white);font-size:10px;padding:8px 22px">Email</div>
  <div class="abs" style="left:532px;top:2673px;width:348px;height:27px;background:var(--olive);color:var(--white);font-size:10px;padding:8px 22px">Phone</div>
  <div class="abs" style="left:532px;top:2714px;width:348px;height:95px;background:var(--olive);color:var(--white);font-size:10px;padding:12px 22px">massage</div>
  <a class="btn" style="left:532px;top:2825px;width:118px;height:43px;background:var(--orange-deep)">Send</a>

  <!-- Community -->
  <h2 class="heading abs" style="left:126px;top:3170px">Join Our Community</h2>
  <p class="copy abs" style="left:128px;top:3225px;width:450px">Lumora Pathis Academy is more than a school—it's a vibrant community where children develop the knowledge, skills, and character to thrive in an ever-changing world. We invite families who believe in our vision of education that connects generations, bridges theory and practice, and nurtures tomorrow's innovative leaders and responsible citizens.</p>
  <div class="abs" style="left:670px;top:3064px;width:389px;height:325px;background:var(--orange-deep)"></div>
  <div class="media" style="left:687px;top:3080px;width:355px;height:418px;background:linear-gradient(160deg,#4a4a4a,#2a2a2a 50%,#f07a30 80%)" role="img" aria-label="Photo of a boy carrying a stack of books in front of a chalkboard"></div>
  <div class="ornament green" style="left:988px;top:3008px;width:150px;height:110px" role="img" aria-label="Decorative green speech bubble"></div>

  <!-- Footer -->
  <div class="abs" style="left:114px;top:3612px;width:266px;text-align:center">
    <div style="width:110px;height:110px;border-radius:50%;background:var(--green);margin:0 auto 14px"></div>
    <div style="font-family:'Lexend',sans-serif;font-weight:400;font-size:34px;line-height:36px;color:#a33a2a">Lumora Pathis<br>Academy</div>
  </div>
  <h3 class="foot-h abs" style="left:404px;top:3590px">QUICK LINKS</h3>
  <a class="foot-link" style="left:405px;top:3629px">Home</a>
  <a class="foot-link" style="left:405px;top:3656px">About Us</a>
  <a class="foot-link" style="left:405px;top:3683px">Our Approach</a>
  <a class="foot-link" style="left:405px;top:3709px">Admissions</a>
  <a class="foot-link" style="left:405px;top:3736px">Academics</a>
  <a class="foot-link" style="left:405px;top:3763px">Community Life</a>
  <a class="foot-link" style="left:405px;top:3789px">News &amp; Blog</a>
  <a class="foot-link" style="left:405px;top:3816px">Contact Us</a>

  <h3 class="foot-h abs" style="left:603px;top:3590px">CONTACT INFO</h3>
  <svg class="abs" style="left:603px;top:3632px" width="14" height="14" viewBox="0 0 14 14"><path d="M3 1 l3 3 -2 2 c1 2 2 3 4 4 l2-2 3 3 -2 2 C6 13 1 8 1 3z" fill="var(--orange-deep)"/></svg>
  <div class="abs foot-small" style="left:625px;top:3628px"><span style="color:#444;font-size:12px">Phone*</span><br>(555) 210-4480</div>
  <svg class="abs" style="left:603px;top:3683px" width="14" height="14"><circle cx="7" cy="7" r="6.5" fill="var(--orange-deep)"/><path d="M7 3 V7 H10" stroke="#fff" stroke-width="1.5" fill="none"/></svg>
  <div class="abs foot-small" style="left:625px;top:3678px"><span style="color:#444;font-size:12px">Hours*</span><br>Mon– Sat: 7:00 AM – 6:00 PM<br>Sunday: Closed</div>
  <svg class="abs" style="left:604px;top:3750px" width="12" height="16"><path d="M6 0 a6 6 0 0 1 6 6 c0 4 -6 10 -6 10 s-6 -6 -6 -10 a6 6 0 0 1 6 -6z" fill="var(--orange-deep)"/><circle cx="6" cy="6" r="2" fill="#fff"/></svg>
  <div class="abs foot-small" style="left:625px;top:3744px"><span style="color:#444;font-size:12px">Location*</span><br>48 Harbor Ln Ste 4<br>Brookvale, WI 53100</div>

  <h3 class="foot-h abs" style="left:832px;top:3592px">NEWSLETTER</h3>
  <p class="abs foot-small" style="left:832px;top:3628px;width:260px">Subscribe to our email address to get the latest news.</p>
  <div class="abs" style="left:832px;top:3673px;width:259px;height:46px;background:var(--white);box-shadow:0 2px 10px rgba(0,0,0,.1);display:flex;align-items:center;padding:0 18px;font-size:11.5px;color:#444">
    <svg width="12" height="9" style="margin-right:8px"><rect width="12" height="9" fill="var(--orange-deep)"/><path d="M0 0 L6 5 L12 0" stroke="#fff" fill="none"/></svg>
    Enter Your Email...
    <svg width="14" height="14" style="margin-left:auto"><path d="M0 6 L14 0 L9 14 L7 8z" fill="var(--orange-deep)"/></svg>
  </div>

  <div class="abs" style="left:87px;top:3851px;width:1026px;height:1px;background:#ddd"></div>
  <p class="abs" style="left:0;top:3878px;width:1200px;text-align:center;font-size:12px;color:#444">© 2025 &nbsp;Lumora Pathis. All rights reserved.</p>
  <span class="social" style="left:972px"></span>
  <span class="social" style="left:1007px"></span>
  <span class="social" style="left:1044px"></span>
  <span class="social" style="left:1078px"></span>
  <svg class="abs" style="left:1130px;top:3822px" width="44" height="44" aria-hidden="true">
    <circle cx="22" cy="22" r="20" fill="var(--orange-deep)"/>
    <circle cx="14" cy="22" r="2.5" fill="#fff"/><circle cx="22" cy="22" r="2.5" fill="#fff"/><circle cx="30" cy="22" r="2.5" fill="#fff"/>
  </svg>

</div>
</body>
</html>
```